Gift Box for a Luxury makeup brush set.

** Please see the updated photo called 'Velmora Crest Inspiration' this is our inspiration for this design concept. Hope that helps!

This project is for a gift box that will hold a luxury makeup brush set.

I have attached the packaging dimensions of the box printing file we need designed (271mm high * 80mm * 80 millimetres). We want the whole box to be in black marble similar to the attached example. This is a gift box and we want it to have a luxurious, high-end feel. All font should be clear but minimal and in sans serif font. On the front it needs to have:

Brand Name/Logo: Velmora Crest (prominently displayed)

And this description: Professional Makeup Brush Set

On the bottom of the box the UPC barcode (file attached) in this size: 48.5 mm x 25.4 mm
Updates

I don’t know how to extend it but we are working to A very tight deadline for this. Hoping to get the designs done sooner. Thanks, Tamsin

Target Market(s)

people looking for an luxury gift, chic beauty lovers, males looking for an expensive looking gift

Font styles to use
Sans Serif

Colors

Designer to choose colors to be used in the design.

Requirements
Must have
• Black marble background
• Brand name/logo
• Description: Professional Makeup Brush Set
• On the bottom of the box the UPC barcode (file attached) in this size: 48.5 mm x 25.4 mm
Should not have
• metallics we can't print foil

```html
<!DOCTYPE html>
<html lang="en">
<head>
<meta charset="utf-8">
<title>Velmora Crest – Gift Box Front Panel</title>
<link rel="stylesheet" href="https://fonts.googleapis.com/css2?family=Montserrat:wght@500;600&display=swap">
<style>
  :root {
    --backdrop: #878787;
    --marble-deep: #0b0b0c;
    --marble-mid: #1c1c1e;
    --marble-vein: #3a3a3d;
    --ink-light: #ffffff;
  }
  html, body {
    margin: 0;
    padding: 0;
    width: 1200px;
    height: 1200px;
    overflow: hidden;
    background: var(--backdrop);
  }
  .canvas {
    position: relative;
    width: 1200px;
    height: 1200px;
    background: var(--backdrop);
  }
  .box-front {
    position: absolute;
    left: 440px;
    top: 60px;
    width: 320px;
    height: 1080px;
    overflow: hidden;
    font-family: "Montserrat", sans-serif;
    color: var(--ink-light);
  }
  .box-front__marble {
    position: absolute;
    inset: 0;
    background:
      radial-gradient(ellipse at 30% 20%, var(--marble-vein) 0%, transparent 45%),
      radial-gradient(ellipse at 75% 65%, var(--marble-mid) 0%, transparent 55%),
      linear-gradient(160deg, var(--marble-mid) 0%, var(--marble-deep) 45%, var(--marble-mid) 75%, var(--marble-deep) 100%);
  }
  .box-front__brand {
    position: absolute;
    left: 0;
    right: 0;
    top: 150px;
    height: 660px;
    display: flex;
    justify-content: center;
    align-items: center;
  }
  .brand-name {
    writing-mode: vertical-rl;
    transform: rotate(180deg);
    font-weight: 600;
    font-size: 66px;
    letter-spacing: 0.04em;
    line-height: 1;
    white-space: nowrap;
    margin: 0;
  }
  .box-front__description {
    position: absolute;
    left: 0;
    right: 0;
    bottom: 150px;
    text-align: center;
    font-weight: 500;
    font-size: 17px;
    line-height: 1.75;
    letter-spacing: 0.42em;
    text-transform: uppercase;
    padding-left: 0.42em;
    margin: 0;
  }
</style>
</head>
<body>
  <main class="canvas">
    <section class="box-front">
      <div class="box-front__marble" role="img" aria-label="Black marble texture with fine white veining"></div>
      <div class="box-front__brand">
        <h1 class="brand-name">VELMORA CREST</h1>
      </div>
      <p class="box-front__description">Professional<br>Makeup<br>Brush Set</p>
    </section>
  </main>
</body>
</html>
```